Up and Coming Software Company needs a universal, cutting edge power point template.

Looking for a PowerPoint template designed for our company 'Lumen Chart Plus'. We supply dental software to practices across North America. I will attach our corporate logo and you can visit our website @ www.lumenchart.example so you can garner an idea of what kind of look and colors we are going for. A somewhat unique slide master would be appreciated, we like a clean, modern approach to our presentations. Our application is designed to save office staff time, increase revenues and eliminate the loss of patients. We are also the most comprehensive patient recall product in the marketplace today.

Target Market(s)

dentists, partner corporations, office managers - 35-50 yrs old

Industry/Entity Type

Dental

Requirements
Must have
• Our Logo, corporate colors. Must be compatible with all recent versions of PowerPoint
Should not have
• Pictures of teeth, toothbrushes etc. Anything cliche with respect to dentistry.

```html
<!DOCTYPE html>
<html lang="en">
<head>
<meta charset="utf-8">
<title>Why Recall? – Lumen Chart Plus</title>
<link href="https://fonts.googleapis.com/css2?family=Montserrat:wght@700&family=Questrial&display=swap" rel="stylesheet">
<style>
  :root {
    --green: #16813f;
    --green-dark: #0f6a32;
    --ink: #2e2e2e;
    --text: #3c3c3c;
    --muted: #8c8c8c;
    --panel: #ffffff;
    --stage-top: #e9e9e9;
    --stage-bottom: #cfcfcf;
    --pill: #bdbdbd;
  }
  * { margin: 0; padding: 0; box-sizing: border-box; }
  html, body { width: 1200px; height: 900px; overflow: hidden; }
  body {
    position: relative;
    font-family: "Questrial", "Century Gothic", sans-serif;
    background: linear-gradient(180deg, var(--stage-top), var(--stage-bottom));
    color: var(--text);
  }
  .panel {
    position: absolute; left: 0; top: 32px; width: 1161px; height: 751px;
    background: radial-gradient(ellipse at 85% 15%, #f3f3f3 0%, var(--panel) 45%);
    box-shadow: 0 2px 8px rgba(0,0,0,.12);
    overflow: hidden;
  }
  .panel-curves { position: absolute; inset: 0; }
  .slide-number {
    position: absolute; left: 28px; top: 0; width: 49px; height: 108px;
    background: var(--green);
    border-radius: 0 0 25px 25px;
    color: #fff; font-family: "Montserrat", sans-serif; font-weight: 700;
    font-size: 22px; display: flex; align-items: flex-end; justify-content: center;
    padding-bottom: 20px;
  }
  .title {
    position: absolute; left: 98px; top: 52px;
    font-family: "Montserrat", sans-serif; font-weight: 700;
    font-size: 68px; color: var(--ink); letter-spacing: -1px;
  }
  .subtitle {
    position: absolute; left: 111px; top: 143px;
    font-size: 24.5px; color: var(--muted);
  }
  .point { position: absolute; left: 80px; width: 1040px; height: 120px; }
  .point-media { position: absolute; left: 0; top: 0; width: 252px; height: 120px; border-radius: 60px; }
  .media-reception { background: linear-gradient(90deg, #d9cfc4, #eeeeec 55%, #c9cccd); }
  .media-handshake { background: linear-gradient(90deg, #4b3526, #8a6b4c 40%, #4f9aa7 75%, #2f8fa0); }
  .media-team { background: linear-gradient(90deg, #e6e6e6, #fafafa 50%, #d8d8d8); }
  .point-body { position: absolute; left: 283px; top: 0; width: 740px; }
  .point-heading { font-size: 26px; color: var(--ink); line-height: 1.2; }
  .point-heading strong { font-family: "Montserrat", sans-serif; font-weight: 700; font-size: 25px; }
  .point-text { margin-top: 12px; font-size: 16.8px; line-height: 22.5px; color: var(--text); }
  .point-list { list-style: none; display: flex; gap: 40px; margin-top: 10px; font-size: 16.8px; }
  .point-list li { position: relative; padding-left: 20px; }
  .point-list li::before {
    content: ""; position: absolute; left: 2px; top: 7px; width: 7px; height: 7px;
    border-radius: 50%; background: var(--green);
  }
  .brand { position: absolute; left: 32px; top: 810px; display: flex; align-items: center; gap: 22px; }
  .brand-mark { width: 60px; height: 60px; border-radius: 50%; background: var(--green); }
  .brand-name { font-family: "Montserrat", sans-serif; font-weight: 700; font-size: 31px; color: var(--green); }
  .contact {
    position: absolute; top: 830px; height: 32px; border-radius: 16px;
    background: var(--pill); color: #fff; font-size: 16.5px;
    display: flex; align-items: center; justify-content: center;
  }
  .contact-web { left: 632px; width: 230px; }
  .contact-phone { left: 888px; width: 273px; gap: 16px; }
</style>
</head>
<body>
  <section class="panel">
    <svg class="panel-curves" width="1161" height="751" viewBox="0 0 1161 751" aria-hidden="true">
      <path d="M780 0 C 1000 120, 1120 320, 1161 520" fill="none" stroke="#efefef" stroke-width="2"/>
      <path d="M880 751 C 1000 600, 1100 480, 1161 420" fill="none" stroke="#f0f0f0" stroke-width="2"/>
    </svg>

    <h1 class="title">Why Recall?</h1>
    <p class="subtitle">Because 70% of your practice revenues depend on it</p>

    <article class="point" style="top:218px">
      <div class="point-media media-reception" role="img" aria-label="Photo of a receptionist at a dental front desk"></div>
      <div class="point-body">
        <h2 class="point-heading"><strong>Patient Recall</strong> - The Pulse Of Your Practice</h2>
        <p class="point-text">Patient recall is the single most important system to the overall success of your practice. Over 70% of practice revenues stem from patient recall so it’s no surprise under-performing recall systems are costing dental practices hundreds of thousands in lost revenues annually.</p>
      </div>
    </article>

    <article class="point" style="top:388px">
      <div class="point-media media-handshake" role="img" aria-label="Photo of a patient shaking hands with a dentist"></div>
      <div class="point-body">
        <h2 class="point-heading"><strong>Stop Losing Patients -</strong> Boost Practice Revenues</h2>
        <p class="point-text">The average practice has thousands of lost and overdue patients.</p>
      </div>
    </article>

    <article class="point" style="top:560px">
      <div class="point-media media-team" role="img" aria-label="Photo of dental staff giving a high five"></div>
      <div class="point-body">
        <h2 class="point-heading"><strong>System Makes Perfect -</strong> Your Staff Will Love You</h2>
        <p class="point-text">Your office staff are busy trying to keep up with everything that needs to get done on a day-to-day basis:</p>
        <ul class="point-list">
          <li>Filling openings</li>
          <li>Serving patients</li>
          <li>Keeping your schedule filled</li>
        </ul>
      </div>
    </article>
  </section>

  <div class="slide-number">01</div>

  <footer>
    <div class="brand">
      <span class="brand-mark"></span>
      <span class="brand-name">Lumen Chart Plus</span>
    </div>
    <div class="contact contact-web">www.lumenchart.example</div>
    <div class="contact contact-phone"><span>Call Toll Free</span><span>1-800-555-0142</span></div>
  </footer>
</body>
</html>
```